Motor Mate 4x6 Flyer

Need 4 x 6 Flyer with following language:

Willow Crest Motor Mate
Our Motor Mate Will Come to Your Home
Our Motor Mate will Drive Your Car to Nearest Gas Station
Our Motor Mate will Fill-up Your Car with Gas
Our Motor Mate will Immediately Return Your Car
Your Car Covered with $100k of Commercial Insurance
Member Dunmore Chamber of Commerce / Honest Merchant League
www.willowcrestmotormate.example

Place logos of Vortan, Brenn & Dorvane on Left Side of Flyer starting at top left corner, mid left side, left bottom corner.
Place logos of BoltNest, 12-Forty, Tesmira on opposite side right.....
Place Willow Crest Motor Mate Logo on both sides of very top that says Willow Crest Motor Mate

Target Market(s)

Upscale Home Owners

Font styles to use
Sans Serif

Colors
F0912C
F2A743
F7CA91
FBE8D2
FDF5EE

Requirements
Must have
• Flyer Must be Bright Orange

```html
<!DOCTYPE html>
<html lang="en">
<head>
<meta charset="utf-8">
<title>Willow Crest Motor Mate Flyer</title>
<link rel="stylesheet" href="https://fonts.googleapis.com/css2?family=Dosis:wght@400&family=Noto+Sans:wght@700;800&display=swap">
<style>
  :root {
    --backdrop: #60706f;
    --paper: #ffffff;
    --flyer-orange: #f8990f;
    --text-light: #ffffff;
    --brand-red: #e0262b;
    --partner-ink: #3a3a3a;
    --partner-mark: #f0912c;
  }
  * { margin: 0; padding: 0; box-sizing: border-box; }
  html, body {
    width: 889px; height: 1200px; overflow: hidden;
    background: var(--backdrop);
  }
  .canvas {
    position: relative; width: 889px; height: 1200px;
    display: flex; align-items: center; justify-content: center;
  }
  .flyer {
    position: relative; width: 760px; height: 1140px;
    background: var(--paper);
    display: grid; grid-template-columns: 121px 517px 122px;
    overflow: hidden;
  }
  .side { position: relative; }
  .main {
    position: relative; background: var(--flyer-orange);
    color: var(--text-light); overflow: hidden;
  }
  .flyer-title {
    position: absolute; left: 32px; right: 26px; top: 74px;
    font-family: "Noto Sans", sans-serif; font-weight: 800;
    font-size: 33px; line-height: 46px; letter-spacing: 0;
    text-align: center; white-space: nowrap;
    padding-bottom: 6px; border-bottom: 2px solid var(--text-light);
  }
  .service {
    position: absolute; left: 25px; right: 12px;
    font-size: 31px; line-height: 38px; white-space: nowrap;
  }
  .service .light { font-family: "Dosis", sans-serif; font-weight: 400; }
  .service .bold { font-family: "Noto Sans", sans-serif; font-weight: 700; font-size: 29px; }
  .website {
    position: absolute; left: 25px; right: 12px; top: 1090px;
    font-family: "Noto Sans", sans-serif; font-weight: 700;
    font-size: 19px; line-height: 24px; white-space: nowrap;
  }
  .brand-mark {
    position: absolute; left: 0; right: 0;
    display: flex; flex-direction: column; align-items: center; gap: 4px;
    font-family: "Noto Sans", sans-serif; font-weight: 700;
    font-size: 14px; line-height: 16px; text-align: center;
    color: var(--brand-red);
  }
  .brand-mark .square {
    width: 20px; height: 20px; border: 2px solid var(--brand-red);
  }
  .partner {
    position: absolute; left: 0; right: 0;
    display: flex; align-items: center; justify-content: center; gap: 6px;
    font-family: "Noto Sans", sans-serif; font-weight: 700;
    font-size: 15px; color: var(--partner-ink);
  }
  .partner .dot {
    width: 10px; height: 10px; border-radius: 50%;
    background: var(--partner-mark); flex: none;
  }
</style>
</head>
<body>
<div class="canvas">
  <article class="flyer">
    <aside class="side side-left">
      <div class="brand-mark" style="top:66px"><span class="square"></span>MOTOR MATE</div>
      <div class="partner" style="top:212px"><span class="dot"></span>Vortan</div>
      <div class="partner" style="top:557px"><span class="dot"></span>Brenn</div>
      <div class="partner" style="top:1054px"><span class="dot"></span>Dorvane</div>
    </aside>

    <section class="main">
      <h1 class="flyer-title">Willow Crest Motor Mate</h1>

      <p class="service" style="top:182px"><span class="light">Our Motor Mate Will</span><br><span class="bold">Come to Your Home</span></p>
      <p class="service" style="top:327px"><span class="light">Our Motor Mate will </span><span class="bold">Drive</span><br><span class="bold">Your Car to Nearest</span><br><span class="bold">Gas Station</span></p>
      <p class="service" style="top:519px"><span class="light">Our Motor Mate will</span><br><span class="bold">Fill-up Your Car with Gas</span></p>
      <p class="service" style="top:682px"><span class="light">Our Motor Mate will </span><span class="bold">Immediately</span><br><span class="bold">Return Your Car</span></p>
      <p class="service" style="top:827px"><span class="light">Your Car Covered with </span><span class="bold">$100k of</span><br><span class="bold">Commercial Insurance</span></p>
      <p class="service" style="top:960px"><span class="light">Member Dunmore Chamber of</span><br><span class="bold">Commerce / Honest Merchant</span><br><span class="bold">League</span></p>

      <p class="website">www.willowcrestmotormate.example</p>
    </section>

    <aside class="side side-right">
      <div class="brand-mark" style="top:66px"><span class="square"></span>MOTOR MATE</div>
      <div class="partner" style="top:208px"><span class="dot"></span>BoltNest</div>
      <div class="partner" style="top:562px"><span class="dot"></span>12-Forty</div>
      <div class="partner" style="top:1060px"><span class="dot"></span>Tesmira</div>
    </aside>
  </article>
</div>
</body>
</html>
```